Vice chair

I'm running for a position as vice chair this will be posted in the lunch room cafeteria in this package i posted logos, my picture, sample of old flyers to give you a idea i also wrote literature need help in putting it together like it to look like a million bucks goal win this election I summited lots of pdf files and jpeg look though them to help with your design feel free to contact me to further assist you
Updates

Would like this to be completed by Wednesday

Target Market(s)

My constituents

Font styles to use
Serif

Colors

Designer to choose colors to be used in the design.

Requirements
Must have
• Make it look clean neat
Nice to have
• Nice background

```html
<!DOCTYPE html>
<html lang="en">
<head>
<meta charset="utf-8">
<title>Vote Marco Delvalle for Vice Chair</title>
<link href="https://fonts.googleapis.com/css2?family=League+Gothic&family=Roboto+Slab:wght@600;700&family=Merriweather:wght@300;700&display=swap" rel="stylesheet">
<style>
  :root {
    --brown: #4a2204;
    --orange: #fe6a00;
    --cream: #fff8c4;
    --red: #e8141a;
    --white: #ffffff;
    --paper: #ffffff;
  }
  * { margin: 0; padding: 0; box-sizing: border-box; }
  html, body { width: 1200px; height: 825px; overflow: hidden; background: var(--paper); }
  .flyer { position: relative; width: 1200px; height: 825px; background: var(--paper); }

  .star-row { position: absolute; left: 0; width: 1200px; height: 30px; }
  .star-row--top { top: 49px; }
  .star-row--bottom { top: 759px; }

  .panel { position: absolute; }
  .panel--slogan { left: 103px; top: 93px; width: 381px; height: 649px; background: var(--brown); }
  .panel--message { left: 484px; top: 93px; width: 278px; height: 649px; background: var(--orange); }
  .panel--portrait { left: 762px; top: 93px; width: 329px; height: 649px; background: var(--cream); }

  .slogan { position: absolute; left: 143px; top: 126px; font-family: "League Gothic", "Oswald", sans-serif; font-size: 92px; line-height: 74px; color: var(--white); letter-spacing: 0.5px; }
  .slogan span { display: block; }
  .slogan .accent { color: var(--orange); }

  .depots { position: absolute; left: 494px; top: 112px; width: 258px; display: flex; justify-content: space-between; }
  .depot { width: 84px; display: flex; flex-direction: column; align-items: center; gap: 6px; }
  .depot__dot { width: 34px; height: 34px; border-radius: 50%; background: var(--cream); }
  .depot__name { font-family: "Merriweather", serif; font-weight: 700; font-size: 9px; color: var(--white); text-align: center; line-height: 11px; }

  .top-stars { position: absolute; left: 826px; top: 126px; width: 206px; height: 30px; }

  .name-band { position: absolute; left: 484px; top: 177px; width: 607px; height: 110px; background: var(--brown); }
  .vote-for { position: absolute; left: 435px; top: 216px; font-family: "League Gothic", "Oswald", sans-serif; font-size: 27px; color: var(--white); letter-spacing: 0.5px; }
  .candidate { position: absolute; left: 517px; top: 196px; font-family: "Roboto Slab", serif; font-weight: 600; font-size: 59px; line-height: 72px; color: var(--white); letter-spacing: 1.5px; white-space: nowrap; }

  .role-box { position: absolute; left: 484px; top: 287px; width: 339px; height: 71px; background: var(--white); }
  .role { position: absolute; left: 522px; top: 298px; font-family: "Roboto Slab", serif; font-weight: 700; font-size: 37px; line-height: 48px; color: var(--red); white-space: nowrap; }

  .message { position: absolute; left: 507px; top: 393px; width: 250px; color: var(--white); font-family: "Merriweather", serif; }
  .message__intro { font-weight: 300; font-size: 10.4px; line-height: 13.2px; }
  .message__pitch { margin-top: 14px; font-weight: 700; font-size: 10.2px; line-height: 13.1px; }
  .message__ask { margin-top: 12px; font-weight: 300; font-size: 15.6px; line-height: 21px; letter-spacing: 0.3px; }

  .portrait { position: absolute; left: 793px; top: 306px; width: 298px; height: 436px;
    background: linear-gradient(180deg, #7a4a2c 0%, #5b3520 45%, #1a0f0a 75%, #0b0706 100%);
    clip-path: polygon(20% 2%, 55% 0%, 78% 8%, 86% 30%, 84% 62%, 100% 82%, 100% 100%, 3% 100%, 14% 78%, 4% 48%, 8% 22%); }
</style>
</head>
<body>
<div class="flyer">
  <svg width="0" height="0" style="position:absolute">
    <defs>
      <symbol id="star" viewBox="-12 -12 24 24">
        <polygon points="0,-12 2.7,-3.72 11.41,-3.71 4.37,1.42 7.05,9.71 0,4.6 -7.05,9.71 -4.37,1.42 -11.41,-3.71 -2.7,-3.72"/>
      </symbol>
      <g id="star-group">
        <use href="#star" x="-12" y="3" width="24" height="24"/>
        <use href="#star" x="22" y="3" width="24" height="24"/>
        <use href="#star" x="56" y="3" width="24" height="24"/>
        <use href="#star" x="89" y="3" width="24" height="24"/>
        <use href="#star" x="123" y="3" width="24" height="24"/>
      </g>
    </defs>
  </svg>

  <svg class="star-row star-row--top" viewBox="0 0 1200 30" aria-hidden="true">
    <use href="#star-group" x="95" fill="#fe6a00"/>
    <use href="#star-group" x="266" fill="#4a2204"/>
    <use href="#star-group" x="439" fill="#4a2204"/>
    <use href="#star-group" x="612" fill="#fe6a00"/>
    <use href="#star-group" x="792" fill="#fe6a00"/>
    <use href="#star-group" x="965" fill="#4a2204"/>
  </svg>

  <div class="panel panel--slogan"></div>
  <div class="panel panel--message"></div>
  <div class="panel panel--portrait"></div>

  <h2 class="slogan">
    <span>BRING</span>
    <span>CHANGE</span>
    <span class="accent">BRING</span>
    <span class="accent">TRUST</span>
    <span>BRING</span>
    <span>PROGRESS</span>
    <span class="accent">BRING</span>
    <span class="accent">NEW VISION</span>
  </h2>

  <div class="depots">
    <div class="depot"><span class="depot__dot"></span><span class="depot__name">Northfield Yard</span></div>
    <div class="depot"><span class="depot__dot"></span><span class="depot__name">Ridgeview Yard</span></div>
    <div class="depot"><span class="depot__dot"></span><span class="depot__name">Harborside Yard</span></div>
  </div>

  <svg class="top-stars" viewBox="0 0 206 30" aria-hidden="true" fill="#e8141a">
    <use href="#star" x="0" y="1" width="28" height="28"/>
    <use href="#star" x="44" y="1" width="28" height="28"/>
    <use href="#star" x="89" y="1" width="28" height="28"/>
    <use href="#star" x="134" y="1" width="28" height="28"/>
    <use href="#star" x="178" y="1" width="28" height="28"/>
  </svg>

  <div class="name-band"></div>
  <span class="vote-for">VOTE FOR</span>
  <h1 class="candidate">MARCO DELVALLE</h1>

  <div class="role-box"></div>
  <p class="role">As VICE CHAIR</p>

  <div class="message">
    <p class="message__intro">I Marco Delvalle for those who dont know me would like to introduce myself. I have always been approachable and helpful whether you are a probationary officer or a veteran operator with knowledge or information. We must protect our union rules for ourselves, our future and most important our children</p>
    <p class="message__pitch">I would like this opportunity to run as your vice chair a person you can trust and believe in me Positive and motivations are my main keys for progress and for change in my campaign. when there are no leaders to look up to one therefore must become one.</p>
    <p class="message__ask">I do believe I ‘m the right person for this position so please come out and support me and vote me as your vice chair</p>
  </div>

  <div class="portrait" role="img" aria-label="Portrait photo of the candidate in glasses and a dark sweater"></div>

  <svg class="star-row star-row--bottom" viewBox="0 0 1200 30" aria-hidden="true">
    <use href="#star-group" x="95" fill="#fe6a00"/>
    <use href="#star-group" x="266" fill="#4a2204"/>
    <use href="#star-group" x="439" fill="#4a2204"/>
    <use href="#star-group" x="612" fill="#fe6a00"/>
    <use href="#star-group" x="792" fill="#fe6a00"/>
    <use href="#star-group" x="965" fill="#4a2204"/>
  </svg>
</div>
</body>
</html>
```